Metal head/ Sushi chef wanting artistic yet high imact business card

I'm sushi chef for make living in Australia originally from Tokyo Japan.
I'm also guitarist/composer as well on progressive metalcore/djent genre.
My favorite visual art is Mandala. Sacred geometries, Fractals, Paisleys are also things fit in me. I like dark color, earth color, and sometimes psychedelic patterns.
I want to hand out my business card when I meet new people in music industries or someone who is wanting private sushi chef for their party.
I know metal and sushi are far different subjects but they are all my passion. I would like to work with the designer who can create something cool from information above.

https://www.vidlorix.com/channel/QX8p4LtRwe7JnVb2kHs9DY3m
https://tunebarrel.com/user-804716273

Front
my name, Haruki Motobe
occupation, "Sushi chef" "Metal guitarist/composer"
Email address, pelvonmist@tavemail.net
Phone number, (61)498201753

Back:
My Vidlorix channel, Friendquay, Tunebarrel, Pictavio. All of those are searchable by "Pelvonmist" The website mentioned above can be described as their logos.

Target Market(s)

people in Music industry, such as musicians, venue managers, promoters.
People who wants to have private sushi chef for their private function, party or events.

Industry/Entity Type

Artists

Contact Information for Business Card

Uploaded photos are just image reference. not thinking to use them.
My details:
I like :
energetic music that has a lot of details such as Progressive metalcore, jazz, djent, psychedelic music.
Spiritual thoughs, Buddism, fundamentals, relaxation music, 420, weed culture, Free thoughts
U.S street culture, skate board, brelks, surf, bicycle, nature, camping, hiking, ocean, mountain, desert, countryside,
permaculture, natural farming, organic farming, compost, self sufficient.
nigiri sushi, art sushi, something/someone beautiful in mind.

Dislike:
Fakes, Bullshits, format, negative, preservatives, artificial colors, illuminati, satanism, manipulation, mass favorites, big society, politics, Chinese letters on western design

Colors
0455a3
000000
7c7c7c
00a990
acd036
f37122

Requirements
Must have
• Front
• my name, Haruki Motobe
• occupation, "Sushi chef" "Metal guitarist/composer"
• Email address, pelvonmist@tavemail.net
• Phone number, (61)498201753
• Back:
• My Vidlorix channel, Friendquay, Tunebarrel, Pictavio. All of those are searchable by "Pelvonmist" The website mentioned above can be described as their logos.
Nice to have
• something based on one of those either back ground or logo:
• Mandala, Sacred Geometry, Fractal art
Should not have
• pop essence. mass favorites, pink, Chinese letters, asian fonts, something asian

```html
<!DOCTYPE html>
<html lang="en">
<head>
<meta charset="utf-8">
<title>Haruki Motobe — Business Card</title>
<link rel="stylesheet" href="https://fonts.googleapis.com/css2?family=Lobster&family=Open+Sans:wght@400;600&display=swap">
<style>
  :root {
    --stage: #1b1b1b;
    --stage-light: #2c2c2c;
    --brand-blue: #0455a3;
    --ink-grey: #555555;
    --paper: #ffffff;
    --mandala-dark: #0d0f16;
    --mandala-navy: #1c2440;
    --mandala-bronze: #5e5540;
    --mandala-steel: #46505e;
  }
  * { margin: 0; padding: 0; box-sizing: border-box; }
  html, body { width: 1200px; height: 900px; overflow: hidden; }
  body {
    background: radial-gradient(ellipse at 50% 40%, var(--stage-light), var(--stage) 70%);
    font-family: "Open Sans", sans-serif;
    position: relative;
  }
  .card {
    position: absolute;
    left: 240px;
    width: 720px;
    height: 400px;
    overflow: hidden;
    box-shadow: 0 10px 30px rgba(0,0,0,.6);
  }
  .card--front { top: 35px; }
  .card--back { top: 465px; }
  .card__pattern {
    position: absolute; inset: 0;
    background:
      radial-gradient(circle at 12% 15%, var(--mandala-navy) 0 9%, var(--mandala-steel) 10% 16%, transparent 17%),
      radial-gradient(circle at 80% 85%, var(--mandala-navy) 0 8%, var(--mandala-bronze) 9% 16%, transparent 17%),
      radial-gradient(circle at 55% 10%, var(--mandala-bronze) 0 6%, transparent 20%),
      radial-gradient(circle at 25% 90%, var(--mandala-steel) 0 8%, transparent 22%),
      linear-gradient(135deg, var(--mandala-dark), #1a1c22 50%, var(--mandala-dark));
  }
  .card__band {
    position: absolute;
    left: 0; right: 0;
    top: 78px; height: 224px;
    background: var(--paper);
    border-top: 4px solid var(--brand-blue);
    border-bottom: 4px solid var(--brand-blue);
    display: flex;
    align-items: center;
    justify-content: center;
  }
  .signature {
    font-family: "Lobster", cursive;
    color: var(--brand-blue);
    font-size: 68px;
    letter-spacing: 1px;
  }
  .card--back .card__band { top: 92px; height: 210px; }
  .identity {
    width: 320px;
    text-align: right;
    padding-right: 20px;
    white-space: nowrap;
  }
  .identity__name {
    color: var(--brand-blue);
    font-weight: 600;
    font-size: 32px;
    letter-spacing: .5px;
    line-height: 1.1;
  }
  .identity__role {
    color: var(--ink-grey);
    font-size: 16px;
    margin-top: 4px;
  }
  .divider {
    width: 2px; height: 110px;
    background: var(--brand-blue);
    flex: none;
  }
  .contact {
    padding-left: 20px;
    width: 380px;
    color: var(--ink-grey);
    font-size: 18px;
    line-height: 1.45;
    white-space: nowrap;
  }
  .contact__line { display: flex; align-items: center; gap: 9px; }
  .contact__line svg { width: 13px; height: 13px; flex: none; }
  .social {
    display: flex; align-items: baseline; gap: 6px;
    margin-top: 8px;
    font-size: 12px;
  }
  .social__name { color: var(--brand-blue); font-weight: 600; }
  .social__handle { font-size: 17px; margin-left: 6px; color: var(--ink-grey); }
</style>
</head>
<body>
  <section class="card card--front">
    <div class="card__pattern" role="img" aria-label="Dark fractal mandala pattern in navy, steel and bronze tones"></div>
    <div class="card__band">
      <p class="signature">Haruki Motobe</p>
    </div>
  </section>

  <section class="card card--back">
    <div class="card__pattern" role="img" aria-label="Dark fractal mandala pattern in navy, steel and bronze tones"></div>
    <div class="card__band">
      <div class="identity">
        <h1 class="identity__name">HARUKI MOTOBE</h1>
        <p class="identity__role">Sushi chef, Metal guitarist/composer</p>
      </div>
      <div class="divider"></div>
      <div class="contact">
        <p class="contact__line">
          <svg viewBox="0 0 16 16" fill="var(--brand-blue)"><path d="M3 1l3 1 1 3-2 1.5c1 2 2.5 3.5 4.5 4.5L11 9l3 1 1 3-2 2C7 15 1 9 1 3z"/></svg>
          (61) 49820 1753
        </p>
        <p class="contact__line">
          <svg viewBox="0 0 16 16" fill="none" stroke="var(--brand-blue)" stroke-width="1.6"><rect x="1" y="3" width="14" height="10"/><path d="M1 3l7 6 7-6"/></svg>
          pelvonmist@tavemail.net
        </p>
        <p class="contact__line">
          <svg viewBox="0 0 16 16" fill="none" stroke="var(--brand-blue)" stroke-width="1.4"><circle cx="8" cy="8" r="7"/><ellipse cx="8" cy="8" rx="3" ry="7"/><path d="M1 8h14"/></svg>
          www.tunebarrel.com
        </p>
        <div class="social">
          <span class="social__name">Vidlorix</span>
          <span class="social__name">Friendquay</span>
          <span class="social__name">Tunebarrel</span>
          <span class="social__name">Pictavio</span>
          <span class="social__handle">Pelvonmist</span>
        </div>
      </div>
    </div>
  </section>
</body>
</html>
```